Postcard needed for expert witness service

Looking for a professional postcard that will be mailed to personal injury lawyers / law firms to introduce my expert witness services.

Target Market(s)

Law firms, personal injury lawyers

Industry/Entity Type

Expert witness, law

Font styles to use
Sans Serif

Requirements
Must have
• Logo: The Frost Counsel [Main Heading]Do you handle snow and ice related slip and falls? Darrel is one of the top snow industry experts in the country! [Following should be in a list type fashion, possibly bulleted]Darrel's credentials: Accredited Winter Practitioner (AWP), past WRTA board member and chair, former ISO 9001 certified snow company owner , 32 years in the industry. (555) 284-3917 NOTES: Postcard will be 4" x 6" Please use both sides however must have room for labels and stamp
Should not have
• Wouldn't suggest using both photos on same side. Honestly, feel free to only use one of the slip and fall photos if it works out better. Thanks!

```html
<!DOCTYPE html>
<html lang="en">
<head>
<meta charset="utf-8">
<title>The Frost Counsel – Postcard</title>
<link href="https://fonts.googleapis.com/css2?family=Montserrat:wght@400&family=Poppins:wght@400;500;600;800;900&display=swap" rel="stylesheet">
<style>
:root{
  --ink:#000;
  --paper:#fff;
  --stage:#1e1e1e;
  --frame:#6e6e6e;
  --rule:#8a8a8a;
  --stamp:#dcdcdc;
  --photo-warm:#6b625d;
}
*{margin:0;padding:0;box-sizing:border-box}
html,body{width:1071px;height:1200px;overflow:hidden;background:var(--stage)}
body{position:relative;font-family:"Poppins",sans-serif;color:var(--ink)}
.card{position:absolute;left:203px;width:663px;height:442px;background:var(--paper);overflow:hidden}
.card--front{top:55px}
.card--back{top:599px}

/* front */
.front-photo{position:absolute;inset:0;
  background:linear-gradient(90deg,var(--photo-warm) 0%,#7d746e 30%,#b7b2ae 46%,#e4e2e0 56%,var(--paper) 64%,var(--paper) 100%);}
.front-frame{position:absolute;left:9px;top:9px;right:8px;bottom:9px;border:2px solid var(--frame)}
.brand{font-family:"Montserrat",sans-serif;font-weight:400;letter-spacing:.5px;white-space:nowrap;line-height:1.05}
.front-brand{position:absolute;right:42px;top:40px;font-size:22px;text-align:right}
.front-question{position:absolute;right:42px;top:103px;text-align:right;font-weight:600;font-size:21px;line-height:28px}
.front-claim{position:absolute;right:46px;top:190px;text-align:right;font-weight:900;font-size:21.5px;line-height:28px;letter-spacing:.2px}
.call-box{position:absolute;left:395px;top:324px;width:268px;height:86px;background:linear-gradient(160deg,#3a3a3a 0%,#000 35%);border-radius:24px 0 0 24px;color:var(--paper);text-align:center;padding-top:18px}
.call-label{font-weight:600;font-size:16px;line-height:18px;display:flex;align-items:center;justify-content:center;gap:5px}
.call-label::before,.call-label::after{content:"";width:24px;height:1.5px;background:currentColor}
.call-number{font-weight:800;font-size:27px;line-height:34px;letter-spacing:.5px}

/* back */
.back-left{position:absolute;left:0;top:0;width:346px;height:442px;background:var(--ink)}
.back-photo{position:absolute;left:0;top:0;width:346px;height:167px;
  background:linear-gradient(90deg,#5b6a86 0%,#8d96a6 35%,#d9dadc 70%,#eeeeee 100%)}
.back-frame{position:absolute;left:11px;top:9px;width:327px;height:424px;border:2px solid var(--frame)}
.cred-head{position:absolute;left:0;top:167px;width:346px;height:34px;background:var(--paper);font-weight:900;font-size:16.5px;line-height:34px;padding-left:36px}
.cred-list{position:absolute;left:36px;top:210px;list-style:none;color:var(--paper);font-size:15.5px;line-height:20px}
.cred-list li{display:flex;align-items:center;gap:9px;white-space:nowrap}
.cred-list svg{width:13px;height:13px;flex:none}
.call-pill{position:absolute;left:0;top:346px;width:317px;height:85px;border-radius:0 24px 24px 0;
  background:linear-gradient(180deg,#f4f4f4 0%,#bcbcbc 35%,#6c6c6c 70%,#cfcfcf 100%);text-align:center;padding:14px 40px 0 0}
.call-pill .call-label{font-size:18px;line-height:22px}
.call-pill .call-number{font-size:28px;line-height:36px}
.back-brand{position:absolute;left:399px;top:44px;font-size:19px}
.stamp{position:absolute;left:572px;top:25px;width:71px;height:75px;background:var(--stamp)}
.address-to{position:absolute;left:399px;top:222px;font-size:15px;font-weight:400}
.address-line{position:absolute;left:399px;width:237px;height:1px;background:var(--rule)}
</style>
</head>
<body>
<section class="card card--front">
  <div class="front-photo" role="img" aria-label="Photo of a woman in a knit hat and winter coat who has slipped and fallen on an icy, snowy path"></div>
  <div class="front-frame"></div>
  <div class="brand front-brand">THE FROST<br>COUNSEL</div>
  <h1 class="front-question">DO YOU HANDLE<br>SNOW &amp; ICE RELATED<br>SLIP &amp; FALLS?</h1>
  <p class="front-claim">DARREL IS ONE OF<br>THE TOP SNOW<br>INDUSTRY EXPERTS<br>IN THE COUNTRY!</p>
  <div class="call-box">
    <div class="call-label">CALL US TODAY!</div>
    <div class="call-number">(555) 284-3917</div>
  </div>
</section>

<section class="card card--back">
  <div class="back-left">
    <div class="back-photo" role="img" aria-label="Photo of a man slipping on a wet icy sidewalk, his backpack falling to the ground"></div>
    <div class="back-frame"></div>
    <h2 class="cred-head">DARREL'S CREDENTIALS:</h2>
    <ul class="cred-list">
      <li><svg viewBox="0 0 16 16"><circle cx="8" cy="8" r="8" fill="#fff"/><path d="M4.5 8.2l2.3 2.3 4.7-4.8" fill="none" stroke="#000" stroke-width="2"/></svg>Accredited Winter Practitioner</li>
      <li><svg viewBox="0 0 16 16"><circle cx="8" cy="8" r="8" fill="#fff"/><path d="M4.5 8.2l2.3 2.3 4.7-4.8" fill="none" stroke="#000" stroke-width="2"/></svg>Past WRTA Board Member &amp; Chair</li>
      <li><svg viewBox="0 0 16 16"><circle cx="8" cy="8" r="8" fill="#fff"/><path d="M4.5 8.2l2.3 2.3 4.7-4.8" fill="none" stroke="#000" stroke-width="2"/></svg>Former ISO 9001 Certified</li>
      <li><svg viewBox="0 0 16 16"><circle cx="8" cy="8" r="8" fill="#fff"/><path d="M4.5 8.2l2.3 2.3 4.7-4.8" fill="none" stroke="#000" stroke-width="2"/></svg>Snow Company Owner</li>
      <li><svg viewBox="0 0 16 16"><circle cx="8" cy="8" r="8" fill="#fff"/><path d="M4.5 8.2l2.3 2.3 4.7-4.8" fill="none" stroke="#000" stroke-width="2"/></svg>32 Years in The Industry</li>
    </ul>
    <div class="call-pill">
      <div class="call-label">CALL US TODAY!</div>
      <div class="call-number">(555) 284-3917</div>
    </div>
  </div>
  <div class="brand back-brand">THE FROST<br>COUNSEL</div>
  <div class="stamp"></div>
  <div class="address-to">TO</div>
  <div class="address-line" style="top:281px"></div>
  <div class="address-line" style="top:321px"></div>
  <div class="address-line" style="top:362px"></div>
  <div class="address-line" style="top:402px"></div>
</section>
</body>
</html>
```